Business card for Cat Cafe

I have started a small business and need a business card designed. The business is a cat cafe, that is, an ordinary cafe that serves coffee and snacks but with a twist - you can bring your cat to play. In fact the idea is to encourage everyone to come and bring your feline friend in order to build community and provide some fun and connections between fellow cat lovers. Themes of the business include;

- Fun
- Discovery
- Connections

The name of the cafe is Brews and Whiskers!

We look forward to seeing what creative ideas you may have!
Updates

Hi,

 Please note the contact details as below;
14 Tarrant Lane, Marlow Vale,
Port Elwin, VIC
3999

Target Market(s)

Cat owners, any age group

Industry/Entity Type

Small Business

Requirements
Must have
• Must include some type of imagery of a cat itself.

```html
<!DOCTYPE html>
<html lang="en">
<head>
<meta charset="UTF-8">
<title>Brews and Whiskers! — Business Card</title>
<link href="https://fonts.googleapis.com/css2?family=Tinos:wght@400&display=swap" rel="stylesheet">
<style>
  :root {
    --backdrop: #cbbdb8;
    --card-dark: #2a2a2a;
    --card-dark-edge: #1c1c1c;
    --card-light: #ffffff;
    --ink-light: #f2f2f2;
    --ink-dark: #1a1a1a;
    --shadow: rgba(40, 30, 28, 0.35);
  }
  * { margin: 0; padding: 0; box-sizing: border-box; }
  html, body {
    width: 865px;
    height: 1200px;
    overflow: hidden;
  }
  body {
    background: var(--backdrop);
    position: relative;
    font-family: "Tinos", "Times New Roman", serif;
  }
  .card {
    position: absolute;
    width: 560px;
    height: 320px;
    box-shadow: 0 10px 24px var(--shadow);
  }
  .card--front {
    left: 220px;
    top: 275px;
    background: linear-gradient(160deg, #3a3a3a 0%, var(--card-dark) 45%, var(--card-dark-edge) 100%);
    color: var(--ink-light);
  }
  .card--back {
    left: 100px;
    top: 630px;
    background: var(--card-light);
    color: var(--ink-dark);
  }
  .brand-mark {
    position: absolute;
    display: block;
  }
  .card--front .brand-mark {
    left: 190px;
    top: 40px;
    width: 120px;
    height: 120px;
  }
  .brand-name {
    font-weight: 400;
    font-size: 28px;
    letter-spacing: 0.5px;
    white-space: nowrap;
  }
  .front-text {
    position: absolute;
    left: 150px;
    top: 185px;
    text-align: center;
  }
  .tagline {
    margin-top: 6px;
    font-size: 14px;
  }
  .back-details {
    position: absolute;
    left: 50px;
    top: 90px;
    text-align: center;
  }
  .address {
    margin-top: 14px;
    font-style: normal;
    font-size: 18px;
    line-height: 1.3;
  }
  .card--back .brand-mark {
    right: 50px;
    top: 60px;
    width: 130px;
    height: 130px;
  }
</style>
</head>
<body>
  <section class="card card--front" aria-label="Business card front">
    <svg class="brand-mark" viewBox="0 0 120 120" aria-hidden="true">
      <circle cx="60" cy="60" r="54" fill="none" stroke="var(--ink-light)" stroke-width="4"/>
    </svg>
    <div class="front-text">
      <h1 class="brand-name">Brews and Whiskers!</h1>
      <p class="tagline">Coffee, Snacks, Bring Your Cat!</p>
    </div>
  </section>

  <section class="card card--back" aria-label="Business card back">
    <div class="back-details">
      <h2 class="brand-name">Brews and Whiskers!</h2>
      <address class="address">
        14 Tarrant Lane, Marlow Vale,<br>
        Port Elwin, VIC<br>
        3999
      </address>
    </div>
    <svg class="brand-mark" viewBox="0 0 140 140" aria-hidden="true">
      <circle cx="70" cy="70" r="63" fill="none" stroke="var(--ink-dark)" stroke-width="5"/>
    </svg>
  </section>
</body>
</html>
```